Simple HVAC & Electrical Contractor Billboard

Leasing a 12'3" H by 49'3" W billboard. I'd like to use our current logo and add a few words to let people know what we do. Looking for a clean simple look.
Our company name is Harold Pruett Mechanical - What we are is Air Conditioning & Electrical Contractors.

Our license numbers are TACLA00052916K & TECL71420 they will need to be visible on the sign somewhere.

I'm not sure how much information I want to see on the sign. I want to keep it clean but some of our contact info is as follows. Office # 555-208-4619 - Webpage hpmexample.com. I feel like most people can search the name to find the contact info they need but I'll defer to the designers to come up with the best design.

I have attached a couple different logos we have used I the past.

```html
<!DOCTYPE html>
<html lang="en">
<head>
<meta charset="utf-8">
<title>Harold Pruett Mechanical – Billboard</title>
<link rel="stylesheet" href="https://fonts.googleapis.com/css2?family=Lato:wght@400&family=Montserrat:wght@700&display=swap">
<style>
  :root {
    --board-blue: #1f6079;
    --brand-red: #e01b2a;
    --ink-white: #ffffff;
    --art-light: #4f8aa3;
    --art-dark: #2a6a84;
  }
  html, body {
    margin: 0;
    padding: 0;
    overflow: hidden;
    background: var(--board-blue);
  }
  .billboard {
    position: relative;
    width: 1200px;
    height: 300px;
    overflow: hidden;
    background: var(--board-blue);
    color: var(--ink-white);
    font-family: "Lato", sans-serif;
  }
  .service-list {
    margin: 0;
    padding: 0;
    list-style: none;
  }
  .service-item {
    position: absolute;
    font-size: 24px;
    line-height: 30px;
    font-weight: 400;
  }
  .service-item--contractors { left: 81px; top: 18px; }
  .service-item--install { left: 85px; top: 106px; }
  .service-item--sectors { left: 83px; top: 192px; }
  .bullet-mark {
    position: absolute;
    left: 46px;
    width: 25px;
    height: 20px;
    fill: var(--brand-red);
  }
  .bullet-mark--one { top: 38px; }
  .bullet-mark--two { top: 128px; }
  .bullet-mark--three { top: 227px; }
  .trade-illustration {
    position: absolute;
    left: 387px;
    top: 6px;
    width: 295px;
    height: 278px;
    border-radius: 50%;
    background: radial-gradient(circle at 50% 45%, var(--art-light), var(--art-dark) 60%, var(--board-blue) 78%);
  }
  .brand-block {
    position: absolute;
    left: 760px;
    top: 0;
    width: 372px;
    text-align: center;
    font-family: "Montserrat", sans-serif;
    font-weight: 700;
  }
  .brand-square {
    display: block;
    margin: 24px auto 0;
    width: 108px;
    height: 108px;
    background: var(--brand-red);
  }
  .brand-name {
    margin: 12px 0 0;
    font-size: 31px;
    line-height: 36px;
    color: var(--ink-white);
    font-weight: 700;
    white-space: nowrap;
  }
  .brand-name-trade {
    display: block;
    font-size: 18px;
    line-height: 22px;
    letter-spacing: 12px;
  }
  .website {
    position: absolute;
    left: 760px;
    top: 225px;
    width: 372px;
    text-align: center;
    font-family: "Montserrat", sans-serif;
    font-weight: 700;
    font-size: 14px;
  }
  .phone-band {
    position: absolute;
    left: 760px;
    top: 250px;
    width: 371px;
    height: 50px;
    background: var(--brand-red);
    font-family: "Montserrat", sans-serif;
    font-weight: 700;
    font-size: 34px;
    line-height: 50px;
    letter-spacing: 4px;
    text-align: center;
  }
  .license-numbers {
    position: absolute;
    left: 1172px;
    top: 150px;
    transform: translate(-50%, -50%) rotate(-90deg);
    font-size: 11px;
    letter-spacing: 0.3px;
    white-space: nowrap;
  }
</style>
</head>
<body>
<main class="billboard">
  <svg class="bullet-mark bullet-mark--one" viewBox="0 0 25 20" aria-hidden="true"><polygon points="0,4 25,0 25,18 0,20"/></svg>
  <svg class="bullet-mark bullet-mark--two" viewBox="0 0 25 20" aria-hidden="true"><polygon points="0,4 25,0 25,18 0,20"/></svg>
  <svg class="bullet-mark bullet-mark--three" viewBox="0 0 25 20" aria-hidden="true"><polygon points="0,4 25,0 25,18 0,20"/></svg>
  <ul class="service-list">
    <li class="service-item service-item--contractors">Mechanical and<br>Electrical Contractors</li>
    <li class="service-item service-item--install">Specializing in Service<br>and Installation</li>
    <li class="service-item service-item--sectors">Servicing Residential,<br>Commercial and<br>Industrial Sectors</li>
  </ul>

  <div class="trade-illustration" role="img" aria-label="Illustration of an electrician in a hard hat surrounded by tools, meters, bulbs, gears and a battery"></div>

  <div class="brand-block">
    <span class="brand-square" aria-hidden="true"></span>
    <p class="brand-name">HAROLD PRUETT<span class="brand-name-trade">MECHANICAL</span></p>
  </div>
  <div class="website">www.hpmexample.com</div>
  <div class="phone-band">555-208-4619</div>
  <div class="license-numbers">TACLA00052916K &amp; TECL71420</div>
</main>
</body>
</html>
```